Option Sheet

We need a one page option sheet with a left to right reading of the five options. It should be a one sheet, multiple colors and definitive separations between options This is used in a sales consultation. Backround or colors not in option need to have the follow RGB value (5 red, 20 green, 63 blue)

We added a smaller text file, please change that point

Target Market(s)

Divorce

Industry/Entity Type

Legal

Requirements
Must have
• 1) All five options left to right
• 2)language included in sheet

```html
<!DOCTYPE html>
<html lang="en">
<head>
<meta charset="utf-8">
<title>Five Option Divorce Sheet</title>
<link href="https://fonts.googleapis.com/css2?family=Montserrat:wght@400;500&display=swap" rel="stylesheet">
<style>
:root{
  --navy:#05143f;
  --white:#ffffff;
  --red:#e8322a;
  --yellow:#e8f55a;
  --salmon:#fc7f72;
  --green:#7ef872;
  --pale:#eaf57a;
  --magenta:#fa4fd1;
  --ink:#2a2a2a;
}
*{box-sizing:border-box;margin:0;padding:0}
html,body{width:1200px;height:1000px;overflow:hidden;background:var(--white)}
body{font-family:"Montserrat",Arial,sans-serif;position:relative}
.sheet{position:absolute;left:53px;top:112px;width:1094px}
.sheet-header{height:166px;background:var(--navy);position:relative;display:flex;align-items:center;justify-content:center}
.header-emblem{position:absolute;left:50%;top:18px;transform:translateX(-50%);width:110px;height:132px;border-radius:6px;background:linear-gradient(#1a2a5c,#0f1f52);opacity:.55}
.sheet-title{position:relative;color:var(--white);font-weight:400;font-size:36px;letter-spacing:1px}
.options{display:flex;margin-top:7px}
.option{display:flex;flex-direction:column}
.option-1{width:194px;--tone:var(--yellow)}
.option-2{width:239px;--tone:var(--salmon)}
.option-3{width:200px;--tone:var(--green)}
.option-4{width:259px;--tone:var(--pale)}
.option-5{width:202px;--tone:var(--magenta)}
.option-visual{height:229px;background:var(--navy);position:relative;overflow:hidden;border-right:1px solid #3b4a78}
.option-number{position:absolute;left:-58px;top:0;width:116px;height:116px;border-radius:50%;background:var(--white)}
.number-label{position:absolute;left:14px;top:38px;color:var(--red);font-size:33px;font-weight:400}
.option-icon{position:absolute;left:50%;top:92px;transform:translateX(-50%);width:96px;height:92px;border-radius:14px;background:var(--tone);opacity:.9}
.option-name{height:43px;background:var(--navy);border-top:2px solid var(--white);display:flex;align-items:center;justify-content:center;color:var(--tone);font-size:16px;font-weight:500;letter-spacing:.3px;border-right:1px solid #3b4a78}
.option-body{height:327px;background:var(--tone);padding:18px 14px 0 14px;color:var(--ink)}
.option-2 .option-body{padding-left:15px}
.option-body h3{font-size:13px;font-weight:400;margin-bottom:14px}
.option-body h3.cons{margin-top:14px}
.option-body ul{list-style:none}
.option-body li{font-size:10.5px;line-height:1.36;margin-bottom:3px;padding-left:7px;text-indent:-7px}
.option-body li::before{content:"• "}
</style>
</head>
<body>
<main class="sheet">
  <header class="sheet-header">
    <div class="header-emblem" role="img" aria-label="Faint scales of justice emblem"></div>
    <h1 class="sheet-title">FIVE OPTION DIVORCE SHEET</h1>
  </header>
  <section class="options">
    <article class="option option-1">
      <div class="option-visual"><div class="option-number"><span class="number-label" style="left:66px">1</span></div>
        <div class="option-icon" role="img" aria-label="Figure relaxing in a rocking chair"></div></div>
      <h2 class="option-name">DO NOTHING</h2>
      <div class="option-body">
        <h3>Advantages:</h3>
        <ul><li>Stay married</li><li>No life Changes</li></ul>
        <h3 class="cons">Disadvantages:</h3>
        <ul><li>Remain unhappy, depressed, anxious</li><li>Money and assets may disappear</li><li>What is going to change?</li></ul>
      </div>
    </article>
    <article class="option option-2">
      <div class="option-visual"><div class="option-number"><span class="number-label" style="left:72px">2</span></div>
        <div class="option-icon" role="img" aria-label="Two people talking across a desk in counseling"></div></div>
      <h2 class="option-name">GO TO COUNSELING</h2>
      <div class="option-body">
        <h3>Advantages:</h3>
        <ul><li>Reconcile marriage</li><li>Help make a better life</li></ul>
        <h3 class="cons">Disadvantages:</h3>
        <ul><li>Past issues are highlighted and may drudge up old wounds</li><li>It may just clarify the reasons you need to separate and/or divorce</li><li>Both parties must be invested and willing to participate</li></ul>
      </div>
    </article>
    <article class="option option-3">
      <div class="option-visual"><div class="option-number"><span class="number-label" style="left:76px">3</span></div>
        <div class="option-icon" role="img" aria-label="Figure hurrying with a wrench and a briefcase"></div></div>
      <h2 class="option-name">DO IT YOURSELF</h2>
      <div class="option-body">
        <h3>Advantages:</h3>
        <ul><li>No attorney fees</li><li>You are your on attorney</li></ul>
        <h3 class="cons">Disadvantages:</h3>
        <ul><li>People often find that what is “fair,” may in fact, not be truly fair</li><li>Often times, people do not know the risks</li><li>Complicated legal system within intrigue rules</li><li>Unsure how to complete the necessary paperwork and meet the deadlines</li></ul>
      </div>
    </article>
    <article class="option option-4">
      <div class="option-visual"><div class="option-number"><span class="number-label" style="left:72px">4</span></div>
        <div class="option-icon" role="img" aria-label="Hands holding a consent form on a clipboard"></div></div>
      <h2 class="option-name">LIMITED REPRESENTATION</h2>
      <div class="option-body">
        <h3>Advantages:</h3>
        <ul><li>Balance between going alone and our limited involvement in the case</li></ul>
        <h3 class="cons">Disadvantages:</h3>
        <ul><li>Our terms may not benefit from our legal knowledge</li><li>The legal consequences of your legal documents will not be explained to you so that you can formulate a plan for handling the rest of your case.</li><li>Your spouse or other parties may cause your legal fees to increase significantly without action on your part</li></ul>
      </div>
    </article>
    <article class="option option-5">
      <div class="option-visual"><div class="option-number"><span class="number-label" style="left:70px">5</span></div>
        <div class="option-icon" role="img" aria-label="Attorney figure with a check mark"></div></div>
      <h2 class="option-name">HIRE US</h2>
      <div class="option-body">
        <h3>Advantages:</h3>
        <ul><li>Gain the full benefits of our experience</li><li>Have a team of Family Law focus attorneys</li><li>Often saves you or makes you money in the long run</li><li>Save you time, energy and stress</li></ul>
        <h3 class="cons">Disadvantages:</h3>
        <ul><li>Initial cost</li></ul>
      </div>
    </article>
  </section>
</main>
</body>
</html>
```